RZ Advisory Business Cards - High End AV / Low Voltage Company

We are low voltage AV company that specializes in high end clients on the residential side and larger businesses on the commercial side. We want something modern, tech looking but also something that is extremely professional looking. We have uploaded our logos and postcards we already have in the field. Along with a picture of one of our wrapped vans. Our website is at www.rzadvisory.example and our primary colors are the orange, green, grey and blue all military color finishes.

We are interesting in the slogans "Matching You with the Ideal Equipment" or "Guiding the Harborlands in Tech"

Target Market(s)

We focus on 70% Commercial and 30% Residential Customers

Industry/Entity Type

Low Voltage, AV Company

Contact Information for Business Card

Name - Dorian Fenwick, Title - Owner, Office Phone - 555-402-7163, Mobile Phone - 555-718-3094, E-Mail - t@rzadvisory.example, Website: www.rzadvisory.example

Font styles to use
Sans Serif

Requirements
Must have
• Must have Name, Title, Work Phone & Mobile, Website and Logo.
Nice to have
• We want something that will impress our higher end clients with a great logo
Should not have
• Too traditional or plain.

```html
<!DOCTYPE html>
<html lang="en">
<head>
<meta charset="utf-8">
<title>RZ Advisory Business Cards</title>
<link href="https://fonts.googleapis.com/css2?family=Jost:wght@400;500;600&display=swap" rel="stylesheet">
<style>
  :root {
    --page: #ffffff;
    --rust-dark: #5a1906;
    --rust-deep: #6e250c;
    --rust-mid: #7a2c10;
    --orange: #ec6535;
    --orange-light: #f2844f;
    --orange-soft: #f49a63;
    --orange-tab: #e8542f;
    --white: #ffffff;
  }
  html, body {
    margin: 0;
    padding: 0;
    width: 1200px;
    height: 729px;
    overflow: hidden;
    background: var(--page);
    font-family: "Jost", sans-serif;
  }
  .canvas {
    position: relative;
    width: 1200px;
    height: 729px;
  }
  .card {
    position: absolute;
    top: 215px;
    width: 450px;
    height: 270px;
    overflow: hidden;
    background: var(--rust-dark);
  }
  .card--front { left: 142px; }
  .card--back { left: 626px; }

  .circuit-texture {
    position: absolute;
    inset: 0;
    background:
      radial-gradient(ellipse 55% 45% at 12% 20%, rgba(122,44,16,0.9), transparent 70%),
      radial-gradient(ellipse 45% 40% at 18% 80%, rgba(110,37,12,0.9), transparent 70%),
      radial-gradient(ellipse 50% 50% at 50% 45%, rgba(122,44,16,0.6), transparent 70%),
      radial-gradient(ellipse 40% 40% at 90% 90%, rgba(95,28,8,0.8), transparent 70%),
      var(--rust-dark);
  }

  .brand {
    position: absolute;
    display: flex;
    align-items: center;
    white-space: nowrap;
  }
  .brand__dot {
    border-radius: 50%;
    flex: none;
    box-sizing: border-box;
  }
  .brand__name {
    font-weight: 600;
    letter-spacing: 1.5px;
    text-transform: uppercase;
    line-height: 1;
  }

  .card--front .brand {
    left: 0; right: 0;
    top: 88px;
    justify-content: center;
    gap: 14px;
  }
  .card--front .brand__dot {
    width: 66px; height: 66px;
    border: 7px solid var(--orange);
  }
  .card--front .brand__name {
    color: var(--orange);
    font-size: 34px;
  }
  .tagline {
    position: absolute;
    left: 0; right: 0;
    top: 200px;
    text-align: center;
    color: var(--white);
    font-size: 17px;
    font-weight: 400;
    letter-spacing: 0.2px;
    margin: 0;
  }

  .back-panel {
    position: absolute;
    left: 0; top: 0;
    width: 225px;
    height: 270px;
    background:
      radial-gradient(ellipse 60% 40% at 20% 15%, rgba(244,154,99,0.55), transparent 70%),
      radial-gradient(ellipse 50% 40% at 80% 85%, rgba(244,154,99,0.45), transparent 70%),
      linear-gradient(135deg, var(--orange-light), var(--orange));
  }
  .card--back .brand {
    left: 0;
    width: 225px;
    top: 108px;
    justify-content: center;
    gap: 9px;
  }
  .card--back .brand__dot {
    width: 42px; height: 42px;
    border: 5px solid var(--rust-dark);
  }
  .card--back .brand__name {
    color: var(--rust-dark);
    font-size: 19px;
  }

  .person {
    position: absolute;
    right: 30px;
    top: 26px;
    text-align: right;
    color: var(--white);
  }
  .person__name {
    margin: 0;
    font-size: 17px;
    font-weight: 400;
    line-height: 1.1;
  }
  .person__title {
    margin: 0;
    font-size: 13px;
    font-weight: 400;
    line-height: 1.2;
  }

  .contact-tab {
    position: absolute;
    left: 227px;
    top: 105px;
    width: 33px;
    height: 130px;
    background: linear-gradient(90deg, var(--orange-light), var(--orange-tab));
  }
  .contact-list {
    position: absolute;
    left: 235px;
    top: 119px;
    margin: 0;
    padding: 0;
    list-style: none;
  }
  .contact-list li {
    display: flex;
    align-items: center;
    height: 26px;
    color: var(--white);
    font-size: 13.5px;
  }
  .contact-list svg {
    width: 14px;
    height: 14px;
    margin-right: 19px;
    flex: none;
  }
  .contact-list .contact--small { font-size: 12.5px; }
</style>
</head>
<body>
<main class="canvas">

  <section class="card card--front">
    <div class="circuit-texture" role="img" aria-label="Faint circuit-board trace pattern on dark rust background"></div>
    <div class="brand">
      <span class="brand__dot"></span>
      <span class="brand__name">RZ Advisory</span>
    </div>
    <p class="tagline">Matching You with the Ideal Equipment</p>
  </section>

  <section class="card card--back">
    <div class="back-panel" role="img" aria-label="Orange panel with light circuit-board trace pattern"></div>
    <div class="brand">
      <span class="brand__dot"></span>
      <span class="brand__name">RZ Advisory</span>
    </div>

    <div class="person">
      <p class="person__name">Dorian Fenwick</p>
      <p class="person__title">(Owner)</p>
    </div>

    <div class="contact-tab"></div>
    <ul class="contact-list">
      <li>
        <svg viewBox="0 0 16 16" fill="none" stroke="#5a1906" stroke-width="1.2"><path d="M3 2l3 1 1 3-2 1c1 2 2 3 4 4l1-2 3 1 1 3-2 1C7 14 2 9 2 4z"/></svg>
        555-402-7163
      </li>
      <li>
        <svg viewBox="0 0 16 16" fill="none" stroke="#5a1906" stroke-width="1.2"><rect x="4.5" y="1.5" width="7" height="13" rx="1.2"/><line x1="7" y1="12.5" x2="9" y2="12.5"/></svg>
        555-718-3094
      </li>
      <li class="contact--small">
        <svg viewBox="0 0 16 16" fill="none" stroke="#5a1906" stroke-width="1.2"><rect x="1.5" y="3.5" width="13" height="9"/><path d="M1.5 3.5l6.5 5 6.5-5M1.5 12.5l5-4.5M14.5 12.5l-5-4.5"/></svg>
        t@rzadvisory.example
      </li>
      <li class="contact--small">
        <svg viewBox="0 0 16 16" fill="none" stroke="#5a1906" stroke-width="1.2"><circle cx="8" cy="8" r="6.5"/><ellipse cx="8" cy="8" rx="3" ry="6.5"/><line x1="1.5" y1="8" x2="14.5" y2="8"/><path d="M2.5 4.8h11M2.5 11.2h11"/></svg>
        www.rzadvisory.example
      </li>
    </ul>
  </section>

</main>
</body>
</html>
```